Redesign of a Reputation Management Website

StandingMend.com Requirement Doc
Reference Site: NameHarbor.com (should NOT copy this site but be patterned in a similar way because we are changing the back end and functionality similar to it)
StandingMend.com is a functional active site that needs a redesign.
FRONT END
Landing / Home Page:
• Should be built with WordPress for ease of use
• Should contain high quality imagery
• Should contain logo
• Should contain Navigation links on top right or top center
1. Personal
2. Business
3. About us
4. Account Login
5. Sign Up
• Should be broken into sections
1. Header – High Quality Image/Slider/Social Media Icons/Contact Info
2. Information
3. Services Personal / Business
4. Sign Up
5. Footer – Links/Contacts/ Social media
6. Sub footer- Info Links
Landing / Home Page Colours:
Main colours should be contrasting light and dark blues like #1A9BFC, #31A5FC and #60BAF7, with minimal green like #77AE00 as an accent colour. The footer and sub footer should be #1C3344
Landing / Home Functional Requirements:
All front end links should link out their individual pages and/or back end processes, this includes navigation menu items, footer links, and sign up and social media buttons. All linked pages should contain I quality information, Graphics, calls to action and sign up options.
Sign up should have two options, Sign up with social media accounts or standard sign up form.
Login should have two options, Login with social media accounts or standard login form.
Target Market(s)
People that are looking to manage their reputation or repair it, or manage their brand, monitor their reputation online
Industry/Entity Type
Management
Number of Pages Required
1 page
Look and feel

```html
<!DOCTYPE html>
<html lang="en">
<head>
<meta charset="utf-8">
<title>Standing Mend – Online Reputation Management</title>
<link href="https://fonts.googleapis.com/css2?family=Open+Sans:wght@300;400;600&display=swap" rel="stylesheet">
<style>
:root{
  --blue-dark:#1a7fd0;
  --blue:#1a9bfc;
  --blue-mid:#31a5fc;
  --blue-light:#60baf7;
  --accent:#77ae00;
  --ink:#2b2b2b;
  --muted:#8a8a8a;
  --band:rgba(255,255,255,.72);
  --panel:rgba(255,255,255,.45);
  --social-a:#1a7fd0;
  --social-b:#31a5fc;
  --mail:#60baf7;
  --page:#ffffff;
}
*{margin:0;padding:0;box-sizing:border-box}
html,body{width:1200px;height:943px;overflow:hidden;background:var(--page)}
body{font-family:'Open Sans',Arial,sans-serif;position:relative;color:var(--ink)}
.hero{position:absolute;left:0;top:0;width:1200px;height:840px;overflow:hidden}
.hero-photo{position:absolute;inset:0;
  background:
   radial-gradient(ellipse 220px 190px at 250px 430px,#ffffff 0%,rgba(255,255,255,0) 70%),
   radial-gradient(ellipse 420px 260px at 650px 330px,#f4f2ef 0%,rgba(244,242,239,0) 75%),
   radial-gradient(ellipse 200px 300px at 1140px 300px,#e4e9dc 0%,rgba(228,233,220,0) 75%),
   linear-gradient(180deg,#efedea 0%,#ebe7e2 38%,#e2d2bf 58%,#dbc6ae 82%,#d8c2a8 100%);}
.header{position:absolute;left:0;top:0;width:1200px;height:109px}
.brand{position:absolute;left:187px;top:28px;display:flex;align-items:center;gap:8px}
.brand-mark{width:22px;height:22px;background:var(--blue-dark);border-radius:50%}
.brand-name{font-size:19px;font-weight:600;color:var(--ink);line-height:1}
.brand-tag{position:absolute;left:30px;top:26px;font-size:8px;color:var(--muted);white-space:nowrap}
.contact{position:absolute;right:172px;top:20px;text-align:right;color:var(--blue);font-size:17px;line-height:35px}
.contact-line{display:flex;align-items:center;justify-content:flex-end;gap:9px}
.nav{position:absolute;left:0;top:109px;width:1200px;height:43px;background:var(--band)}
.nav-icons{position:absolute;left:200px;top:15px;display:flex;gap:8px}
.nav-links{position:absolute;left:317px;right:172px;top:0;height:43px;display:flex;justify-content:space-between;align-items:center;list-style:none;font-size:13px;color:var(--ink);letter-spacing:.2px}
.nav-links .nav-cta{color:var(--blue);font-weight:600}
.hero-title{position:absolute;left:0;width:1200px;top:228px;text-align:center;font-weight:300;font-size:48px;line-height:51px;color:var(--blue-dark)}
.hero-rule{position:absolute;left:436px;top:361px;width:328px;height:1px;background:#b8b4ae}
.hero-sub{position:absolute;left:0;width:1200px;top:383px;text-align:center;font-weight:300;font-size:22px;line-height:45px;color:var(--blue)}
.signup{position:absolute;left:218px;top:533px;width:840px;height:161px;background:var(--panel)}
.signup-label{position:absolute;left:175px;top:32px;font-size:13px;letter-spacing:.5px}
.social{position:absolute;top:73px;width:44px;height:44px;color:#fff;font-size:9px;display:flex;align-items:center;justify-content:center}
.social-a{left:175px;background:var(--social-a)}
.social-b{left:228px;background:var(--social-b)}
.or{position:absolute;left:293px;top:86px;font-size:13px}
.social-mail{left:330px;background:var(--mail)}
.call{position:absolute;left:428px;top:77px;width:181px;height:30px;border:1px solid #555;font-size:13px;color:var(--blue-dark);display:flex;align-items:center;justify-content:center}
.call-icon{position:absolute;left:622px;top:80px}
.services-title{position:absolute;left:0;width:1200px;top:904px;text-align:center;font-weight:300;font-size:40px;line-height:54px;letter-spacing:2px;color:var(--accent)}
</style>
</head>
<body>
<section class="hero">
  <div class="hero-photo" role="img" aria-label="Soft photo of a person typing on a laptop at a wooden table beside a coffee mug and a plant"></div>

  <header class="header">
    <div class="brand">
      <span class="brand-mark"></span>
      <span class="brand-name">Standing Mend</span>
      <span class="brand-tag">Reputation Consulting Since 1992</span>
    </div>
    <div class="contact">
      <div class="contact-line">
        <svg width="12" height="16" viewBox="0 0 12 16"><path d="M3 1 L5 1 L6 5 L4 6 Q5 10 8 11 L9 9 L12 11 L11 14 Q4 14 1 4 Z" fill="#b5b5b5"/></svg>
        <span>+1 888 555 0142</span>
      </div>
      <div class="contact-line">
        <svg width="18" height="12" viewBox="0 0 18 12"><rect x=".5" y=".5" width="17" height="11" fill="#d0d0d0"/><path d="M.5 .5 L9 7 L17.5 .5" stroke="#fff" fill="none"/></svg>
        <span>Hello@StandingMend.com</span>
      </div>
    </div>
  </header>

  <nav class="nav">
    <div class="nav-icons">
      <svg width="12" height="11" viewBox="0 0 12 11"><path d="M6 0 L12 5 L10 5 L10 11 L2 11 L2 5 L0 5 Z" fill="#999"/></svg>
      <svg width="11" height="11" viewBox="0 0 11 11"><circle cx="5.5" cy="5.5" r="5.5" fill="#999"/></svg>
    </div>
    <ul class="nav-links">
      <li>PERSONAL</li><li>BUSINESS</li><li>REPUTATION</li><li>REPAIR</li><li>SERVICES</li><li>ABOUT US</li><li>ACCOUNT LOGIN</li><li class="nav-cta">SIGN UP</li>
    </ul>
  </nav>

  <h1 class="hero-title">Control and protect<br>Your Online Reputation</h1>
  <div class="hero-rule"></div>
  <p class="hero-sub">Ranked One of the Worlds Leading<br>Internet Reputation Management Specialists</p>

  <div class="signup">
    <p class="signup-label">Sign Up For Free With:</p>
    <span class="social social-a">Friendly</span>
    <span class="social social-b">Chirper</span>
    <span class="or">or</span>
    <span class="social social-mail">
      <svg width="32" height="24" viewBox="0 0 32 24"><path d="M2 9 L16 1 L30 9 L30 23 L2 23 Z" fill="none" stroke="#fff" stroke-width="2"/><path d="M2 9 L16 17 L30 9 M2 23 L12 15 M30 23 L20 15" fill="none" stroke="#fff" stroke-width="2"/></svg>
    </span>
    <span class="call">Call us at (646) 555-0187</span>
    <svg class="call-icon" width="13" height="21" viewBox="0 0 13 21"><rect x="1" y="1" width="11" height="19" rx="2" fill="none" stroke="#111" stroke-width="2"/><rect x="3" y="4" width="7" height="11" fill="#111"/></svg>
  </div>
</section>

<h2 class="services-title">SERVICES</h2>
</body>
</html>
```